International freight forwarder experienced in perishable handling needs a web design

We need a website designed that will allow us to capture more customers through the website. We would like a visually appealing design that is not so heavy on text. Our business covers the logistics and freight forwarding industries and we have offices in South America and the USA. Our main customers are importers USA, Europe, Asia and Russia and we currently work almost exclusively with perishable products such as fresh cut flowers, fresh exotics fruits, cacao, fresh fish etc. We would like to convey a fresh, modern approach to freight forwarding focusing on concepts such as - time sensitive, anytime-anywhere delivery, innovation, experience, reliability and confidence. Should include links with Plumetta and Worvanet. Our core solutions include: Core Services
*Air Freight
*Ocean Freight
*Warehousing & Distribution
Our industry solutions cover
*Flowers
*FMCG including, fruits, vegetables
*Live animals
*Automotive
*Consumer Goods
*Industrial
*Oil & Gas
*Pharma
* Event logistics
* Project logistics

Target Market(s)

Importers in Europe, USA, Asia, Middle East and Russia

Number of Pages Required

4 page

Font styles to use
Sans Serif

Colors
a1cd39
606060
000000

Requirements
Must have
• Photos of fresh cut flowers, FMCG such as cacao, fresh fish (packaged for shipping), fresh exotic fruits, pharma products (packaged for shipping), oil and gas etc. Internal customer login access
Nice to have
• Photos of cargo shipping carriers and cargo airline carriers. Features similar to those of following website http://www.brolvacargo.com/eng/main/index.jsp?FromURL=web
Should not have
• Too much text, needs to be visually pleasing

```html
<!DOCTYPE html>
<html lang="en">
<head>
<meta charset="utf-8">
<title>Verdanta Freight</title>
<link rel="stylesheet" href="https://fonts.googleapis.com/css2?family=Advent+Pro:wght@300;500;600&family=Dosis:wght@500;600;700&family=Lato:wght@300;400&display=swap">
<style>
:root{
  --green:#a1cd39;
  --grey:#606060;
  --black:#000;
  --topbar:#0d0609;
  --footer:#2f3538;
  --footer-base:#1e2224;
  --steel:#4a7ca4;
  --white:#fff;
}
*{box-sizing:border-box;margin:0;padding:0}
html,body{width:1038px;height:1200px;overflow:hidden;background:var(--white)}
body{position:relative;font-family:"Dosis",sans-serif}
.topbar{position:absolute;left:0;top:0;width:1038px;height:30px;background:var(--topbar);color:var(--white);font:600 9px "Dosis",sans-serif}
.topbar .contact{position:absolute;left:80px;top:9px;display:flex;gap:8px;align-items:center}
.topbar .social{position:absolute;left:860px;top:0;display:flex;height:30px}
.topbar .social span{width:28px;height:30px;border-top:2px solid var(--steel);display:flex;align-items:center;justify-content:center;font-size:7px}
.topbar .social span:nth-child(2){border-color:#c0392b}
.header{position:absolute;left:0;top:30px;width:1038px;height:109px;background:var(--white)}
.brand{position:absolute;left:80px;top:22px;display:flex;flex-direction:column;align-items:center;gap:4px}
.brand .dot{width:32px;height:32px;border-radius:50%;background:var(--green)}
.brand .name{font:600 21px "Advent Pro",sans-serif;color:var(--grey);letter-spacing:-.3px}
.brand .group{font:500 6px "Dosis",sans-serif;color:#888;letter-spacing:2px}
.nav{position:absolute;right:78px;top:48px;display:flex;gap:22px;font:600 9px "Dosis",sans-serif;color:var(--green);text-transform:uppercase}
.nav svg{vertical-align:-2px;margin-right:4px}
.hero{position:absolute;left:0;top:139px;width:1038px;height:316px;background:linear-gradient(90deg,#b9cfe4 0%,#8a6a4a 40%,#9b7656 65%,#c9d3df 100%)}
.hero-card{position:absolute;left:77px;top:128px;width:279px;height:136px;background:rgba(20,20,20,.82);color:var(--white);padding:22px 24px;font:300 27px/30px "Advent Pro",sans-serif}
.hero-card b{font-weight:600}
.band{position:absolute;left:0;top:455px;width:1038px;height:150px;background:var(--green)}
.band p{position:absolute;left:78px;top:52px;width:650px;color:var(--white);font:300 26px/30px "Advent Pro",sans-serif}
.btn{position:absolute;display:flex;align-items:center;justify-content:center;gap:10px;color:var(--white);font:600 18px "Dosis",sans-serif}
.btn-office{left:756px;top:59px;width:175px;height:41px;background:var(--black);border:1px solid var(--white)}
.services{position:absolute;left:0;top:605px;width:1038px;height:288px;background:linear-gradient(90deg,#d8d2c8 0%,#c9b59a 45%,#8d7a8e 65%,#d9d4cc 100%)}
.services .veil{position:absolute;left:0;top:50px;width:1038px;height:227px;background:rgba(255,255,255,.72)}
.services p{position:absolute;left:379px;top:118px;width:600px;color:#333;font:300 22px/26px "Lato",sans-serif}
.btn-services{left:843px;top:217px;width:117px;height:41px;background:var(--steel);border:1px solid var(--white);font-size:13px;gap:8px}
.footer{position:absolute;left:0;top:893px;width:1038px;height:253px;background:var(--footer);color:var(--white)}
.footer .brand{left:80px;top:22px}
.footer .brand .name{color:#9aa0a2}
.footer .about{position:absolute;left:77px;top:112px;width:420px;font:700 9.5px/15px "Dosis",sans-serif}
.footer .mail{position:absolute;left:77px;top:184px;width:418px;height:31px;border:1px solid var(--white);display:flex;align-items:center;justify-content:center;gap:6px;font:400 10px "Lato",sans-serif}
.footer .social-title{position:absolute;left:756px;top:40px;width:192px;padding:0 0 4px 5px;border-bottom:1px solid var(--white);font:400 14px "Advent Pro",sans-serif}
.footer .social{position:absolute;left:756px;top:74px;display:flex;background:var(--black)}
.footer .social span{width:28px;height:25px;border-top:2px solid var(--steel);display:flex;align-items:center;justify-content:center;font:600 6px "Dosis",sans-serif}
.footer .social span:nth-child(2){border-color:#c0392b}
.base{position:absolute;left:0;top:1146px;width:1038px;height:54px;background:var(--footer-base);color:var(--white);font:400 9px "Lato",sans-serif;padding:26px 0 0 77px}
</style>
</head>
<body>
<div class="topbar">
  <div class="contact">
    <span>&#9990; +1 (555) 201-0448</span><span>|</span>
    <span><svg width="9" height="7" viewBox="0 0 9 7"><rect x=".5" y=".5" width="8" height="6" fill="none" stroke="#fff"/><path d="M.5 .5 4.5 4 8.5 .5" fill="none" stroke="#fff"/></svg> mail@verdantafreight.com</span>
  </div>
  <div class="social"><span>Plumetta</span><span>Gravio</span><span><svg width="10" height="8" viewBox="0 0 10 8"><rect x=".5" y=".5" width="9" height="7" fill="none" stroke="#fff"/><path d="M.5 .5 5 4.5 9.5 .5" fill="none" stroke="#fff"/></svg></span><span>Worvanet</span></div>
</div>

<header class="header">
  <div class="brand"><span class="dot"></span><span class="name">Verdanta Freight</span><span class="group">GROUP</span></div>
  <nav class="nav"><span>Home</span><span>Page 1</span><span>Page 2</span><span>About us</span><span><svg width="11" height="8" viewBox="0 0 11 8"><rect x=".5" y=".5" width="10" height="7" fill="none" stroke="#a1cd39"/><path d="M.5 .5 5.5 4.5 10.5 .5" fill="none" stroke="#a1cd39"/></svg>Contact</span></nav>
</header>

<section class="hero" role="img" aria-label="Photo of air cargo pallets of boxed perishables being loaded into a freighter aircraft">
  <div class="hero-card"><b>Verdanta Freight</b>:<br>Your trusted logistics partner.</div>
</section>

<section class="band">
  <p>Premier logistics service provider with strongest distribution network.</p>
  <a class="btn btn-office">Locate an office <svg width="24" height="24" viewBox="0 0 24 24"><circle cx="12" cy="12" r="10.5" fill="none" stroke="#fff" stroke-width="2"/><path d="M6.5 12h10M12.5 8l4 4-4 4" fill="none" stroke="#fff" stroke-width="2"/></svg></a>
</section>

<section class="services" role="img" aria-label="Photo of netted flower and produce cargo inside an aircraft hold">
  <div class="veil"></div>
  <p>With a global network across six continents and strong partnerships with major air, ocean and road carriers, international freight forwarding is one of our core services.</p>
  <a class="btn btn-services">Our Services <svg width="24" height="24" viewBox="0 0 24 24"><circle cx="12" cy="12" r="10.5" fill="none" stroke="#fff" stroke-width="2"/><path d="M6.5 12h10M12.5 8l4 4-4 4" fill="none" stroke="#fff" stroke-width="2"/></svg></a>
</section>

<footer class="footer">
  <div class="brand"><span class="dot"></span><span class="name">Verdanta Freight</span><span class="group">GROUP</span></div>
  <p class="about">Here goes some short description about company- Lorem ipusum. Add you content. Here goes some short description about company- Lorem ipusum. Add you content. Here goes some short description about company- Lorem ipusum. Add you content. Here goes some short description about company- Lorem ipusum. Add you content.</p>
  <div class="mail"><svg width="11" height="10" viewBox="0 0 11 10"><path d="M10.5 .5 .5 4.5 4 5.5 5 9.5 6.5 6.5 10.5 .5Z" fill="#fff"/></svg> info@verdantafreight.com</div>
  <h3 class="social-title">We are social</h3>
  <div class="social"><span>Plumetta</span><span>Gravio</span><span><svg width="10" height="8" viewBox="0 0 10 8"><rect x=".5" y=".5" width="9" height="7" fill="none" stroke="#fff"/><path d="M.5 .5 5 4.5 9.5 .5" fill="none" stroke="#fff"/></svg></span><span>Worvanet</span></div>
</footer>

<div class="base">Copyright &copy; 2015 Verdanta Freight</div>
</body>
</html>
```